Finally a Vodka produced for women ! (Label Design)

We are a small distillery based in Melbourne, Australia and we need a Vodka label design solution that will appeal to women aged 30-50 years and radiate luxury. Full Details are in a design brief attached. We thank you in advance.

Target Market(s)

Affluent females 30-50 years.

Industry/Entity Type

Spirits/Alcohol

Requirements
Must have
• Be clear this is a luxury Vodka.
Nice to have
• Elegance.

```html
<!DOCTYPE html>
<html lang="en">
<head>
<meta charset="utf-8">
<title>Silver Wren Distillery – Premium Vodka Label</title>
<link rel="stylesheet" href="https://fonts.googleapis.com/css2?family=Marcellus&family=Cinzel:wght@400&family=Quicksand:wght@400;700&family=Libre+Baskerville:wght@700&display=swap">
<style>
  :root {
    --canvas: #ffffff;
    --plum: #2d0f21;
    --ink: #111111;
    --neck-black: #0c0c0c;
    --silver-light: #ffffff;
    --silver-mid: #d9d9d9;
    --silver-dark: #8f8f8f;
    --pearl: #ecebeb;
    --rose-tone: #f1eff0;
  }
  html, body {
    margin: 0;
    width: 1200px;
    height: 1200px;
    overflow: hidden;
    background: var(--canvas);
  }
  .canvas {
    position: relative;
    width: 1200px;
    height: 1200px;
  }
  .label {
    position: absolute;
    left: 317px;
    top: 31px;
    width: 566px;
    height: 1138px;
    display: block;
  }
  .label-ground { fill: var(--plum); }
  .neck-band { fill: var(--neck-black); }
  .abv {
    font-family: "Libre Baskerville", "Times New Roman", serif;
    font-weight: 700;
    font-size: 19px;
    fill: var(--silver-mid);
  }
  .brand-name {
    font-family: "Quicksand", "Helvetica Neue", sans-serif;
    font-weight: 700;
    fill: var(--ink);
  }
  .brand-name--main { font-size: 40px; letter-spacing: 7px; }
  .brand-name--sub { font-size: 16px; letter-spacing: 5px; }
  .product-name {
    font-family: "Marcellus", "Georgia", serif;
    font-size: 104px;
    fill: var(--pearl);
  }
  .grade {
    font-family: "Cinzel", "Georgia", serif;
    font-size: 30px;
    letter-spacing: 13px;
    fill: #1a1a1a;
  }
  .rose-art { fill: var(--rose-tone); }
  .tagline {
    font-family: "Quicksand", "Helvetica Neue", sans-serif;
    font-weight: 400;
    font-size: 45px;
    fill: var(--silver-mid);
  }
  .volume {
    font-family: "Libre Baskerville", "Times New Roman", serif;
    font-weight: 700;
    font-size: 50px;
    fill: var(--ink);
  }
</style>
</head>
<body>
<main class="canvas">
  <svg class="label" viewBox="0 0 652 1312" xmlns="http://www.w3.org/2000/svg" aria-label="Silver Wren Distillery premium vodka label">
    <defs>
      <linearGradient id="silver" x1="0" y1="0" x2="1" y2="0">
        <stop offset="0" stop-color="var(--silver-dark)"/>
        <stop offset="0.45" stop-color="var(--silver-light)"/>
        <stop offset="0.6" stop-color="var(--silver-light)"/>
        <stop offset="1" stop-color="var(--silver-dark)"/>
      </linearGradient>
      <linearGradient id="silver-soft" x1="0" y1="0" x2="1" y2="0">
        <stop offset="0" stop-color="#a9a9a9"/>
        <stop offset="0.5" stop-color="#ffffff"/>
        <stop offset="1" stop-color="#b4b4b4"/>
      </linearGradient>
    </defs>

    <rect class="label-ground" x="0" y="0" width="652" height="1312"/>

    <!-- bottle cap -->
    <rect class="cap" x="240" y="5" width="190" height="74" rx="6" fill="url(#silver)"/>

    <!-- neck band -->
    <rect class="neck-band" x="236" y="77" width="198" height="88"/>
    <text class="abv" x="335" y="140" text-anchor="middle">40% ALC/VOL</text>

    <!-- shoulder shield with distillery name -->
    <polygon class="shoulder" points="230,162 440,162 528,450 326,572 144,450" fill="url(#silver)"/>
    <text class="brand-name brand-name--main" x="330" y="330" text-anchor="middle">SILVER</text>
    <text class="brand-name brand-name--main" x="330" y="378" text-anchor="middle">WREN</text>
    <text class="brand-name brand-name--sub" x="333" y="410" text-anchor="middle">DISTILLERY</text>

    <!-- product name -->
    <text class="product-name" x="340" y="705" text-anchor="middle">Vodka</text>

    <!-- grade band -->
    <polygon class="grade-band" points="120,737 566,737 552,790 106,790" fill="url(#silver-soft)"/>
    <text class="grade" x="340" y="776" text-anchor="middle">PREMIUM</text>

    <!-- rose artwork area -->
    <rect class="rose-art" x="215" y="827" width="250" height="245" rx="110" role="img" aria-label="Stylised silver rose illustration"/>

    <!-- tagline -->
    <text class="tagline" x="340" y="1126" text-anchor="middle">Rose Quartz filtered</text>

    <!-- volume pennant -->
    <polygon class="volume-pennant" points="92,1177 586,1177 340,1312" fill="url(#silver-soft)"/>
    <text class="volume" x="338" y="1252" text-anchor="middle">700ML</text>
  </svg>
</main>
</body>
</html>
```